Holiday PROMO Flyer for Healthy Restaurant

Hi ! We need a holiday style promo flyer for Verandel . Please have a holiday vibe type of design in the background. Include at least 1 of the photos that I provide, and our logo of course. This promo is for a new package that we will be offering until December 31st 2022.

It will have a promo of some type of design that says the following in a creative way:
" HOLIDAY PACKAGE PROMO!"
Buy our holiday package of $500 and receive a $100 gift card!" (THIS SHOULD BE VERY NOTICEABLE AS THIS IS THE ACTUAL PROMO)
Our biggest promo to date.
Offer ends December 31st, 2022.

Take a look at our website to stay consistant with the brand as well.

Industry/Entity Type

Restaurant

Requirements
Must have
• Logo, food photo and gift card photo

```html
<!DOCTYPE html>
<html lang="en">
<head>
<meta charset="UTF-8">
<title>Verandel Holiday Package Promo</title>
<link rel="stylesheet" href="https://fonts.googleapis.com/css2?family=Poppins:wght@400;500;600;700;800;900&family=Yellowtail&display=swap">
<style>
  :root {
    --lime: #a6d11e;
    --lime-bright: #b9e71a;
    --green-mid: #8fb04a;
    --green-soft: #9dbb5c;
    --navy: #1d3263;
    --card-navy: #0f2e5e;
    --brown: #6a4a06;
    --white: #ffffff;
    --paper: #fbfbfb;
    --grey: #9a9a9a;
    --ink: #1b1b1b;
    --page: #f1f1f1;
  }
  * { box-sizing: border-box; margin: 0; padding: 0; }
  html, body { width: 1200px; height: 1200px; overflow: hidden; }
  body { background: var(--page); font-family: "Poppins", sans-serif; position: relative; }

  .poster {
    position: absolute; left: 200px; top: 10px;
    width: 800px; height: 1180px;
    background: var(--paper);
    overflow: hidden;
  }
  .poster__sky {
    position: absolute; left: 0; top: 0; width: 800px; height: 640px;
    background:
      radial-gradient(ellipse at 50% 45%, rgba(255,255,255,0.18), transparent 60%),
      linear-gradient(160deg, var(--green-soft) 0%, var(--green-mid) 45%, var(--lime-bright) 100%);
  }
  .poster__swoosh { position: absolute; left: 0; top: 520px; width: 800px; height: 200px; }

  .headline { position: absolute; left: 0; width: 800px; text-align: center; }
  .headline--script {
    top: 60px;
    font-family: "Yellowtail", cursive;
    font-size: 130px; line-height: 1;
    color: var(--white);
    -webkit-text-stroke: 3px #5f8a18;
    paint-order: stroke fill;
    transform: rotate(-4deg);
  }
  .headline--package {
    top: 205px;
    font-weight: 800; font-size: 150px; line-height: 1;
    letter-spacing: -4px;
    color: var(--navy);
    -webkit-text-stroke: 6px var(--white);
    paint-order: stroke fill;
    text-shadow: 4px 4px 0 rgba(0,0,0,0.25);
  }
  .headline--promo {
    top: 375px;
    font-weight: 800; font-size: 84px; line-height: 1;
    color: var(--brown);
    -webkit-text-stroke: 5px var(--white);
    paint-order: stroke fill;
  }
  .promo-tails { position: absolute; left: 130px; top: 400px; width: 540px; height: 50px; }
  .promo-rule {
    position: absolute; left: 185px; top: 482px; width: 430px;
    border-top: 2px dotted rgba(255,255,255,0.85);
  }

  .food-photo {
    position: absolute; left: 50px; top: 520px; width: 700px; height: 330px;
    border-radius: 160px 160px 120px 120px;
    background:
      radial-gradient(ellipse at 50% 40%, #c98a3e 0%, #7a4a26 35%, transparent 62%),
      radial-gradient(ellipse at 15% 55%, #e9e4da 0%, #d9a56a 25%, transparent 45%),
      radial-gradient(ellipse at 85% 55%, #efe9e0 0%, #b58a57 25%, transparent 45%);
  }

  .offer { position: absolute; left: 60px; top: 895px; width: 690px; height: 195px; }
  .gift-card {
    position: absolute; left: 0; top: 0; width: 262px; height: 186px;
    background: var(--card-navy); border-radius: 10px;
    box-shadow: 0 6px 14px rgba(0,0,0,0.25);
    overflow: hidden;
  }
  .gift-card__band-v { position: absolute; left: 40px; top: 0; width: 14px; height: 100%; background: var(--lime); }
  .gift-card__band-h { position: absolute; left: 0; top: 28px; width: 100%; height: 14px; background: var(--lime); }
  .gift-card__label {
    position: absolute; left: 8px; top: 140px;
    transform: rotate(90deg); transform-origin: left top;
    font-size: 12px; font-weight: 600; letter-spacing: 3px; color: var(--lime);
    left: 30px; top: 70px;
  }
  .gift-card__name {
    position: absolute; left: 70px; top: 86px;
    font-size: 34px; font-weight: 700; color: var(--white); letter-spacing: 1px;
  }
  .gift-card__tag {
    position: absolute; left: 71px; top: 128px;
    font-size: 10.5px; font-weight: 600; color: var(--lime);
  }
  .offer__box {
    position: absolute; left: 262px; top: 6px; width: 398px; height: 188px;
    border: 2px dashed #bdbdbd; border-left: none; border-radius: 0 14px 14px 0;
    padding: 12px 0 0 46px;
  }
  .offer__lead { font-size: 28px; font-weight: 500; color: var(--navy); line-height: 1.15; letter-spacing: -0.5px; }
  .offer__reward { margin-top: 4px; font-size: 43px; font-weight: 800; color: var(--lime); line-height: 1.05; letter-spacing: -0.5px; }

  .footer { position: absolute; left: 0; top: 1120px; width: 800px; height: 60px; }
  .brand { position: absolute; left: 45px; top: -10px; display: flex; flex-direction: column; }
  .brand__row { display: flex; align-items: center; gap: 8px; }
  .brand__dot { width: 10px; height: 10px; border-radius: 50%; background: var(--lime); }
  .brand__name { font-size: 46px; font-weight: 700; color: var(--grey); letter-spacing: 1px; line-height: 1; }
  .brand__tag { font-size: 15px; font-weight: 700; color: var(--lime); margin-top: 4px; margin-left: 18px; }
  .footer__note { position: absolute; right: 55px; top: -6px; text-align: right; }
  .footer__claim { font-size: 22px; font-weight: 800; color: var(--lime); letter-spacing: -0.3px; }
  .footer__date { font-size: 16px; font-weight: 500; color: var(--ink); }
</style>
</head>
<body>
  <main class="poster">
    <div class="poster__sky"></div>
    <svg class="poster__swoosh" viewBox="0 0 800 200" preserveAspectRatio="none">
      <path d="M0 130 Q400 -20 800 70 L800 90 Q400 10 0 150 Z" fill="#a9a9a9"/>
      <path d="M0 150 Q400 10 800 90 L800 200 L0 200 Z" fill="#fbfbfb"/>
    </svg>

    <div class="headline headline--script">Holiday</div>
    <div class="headline headline--package">PACKAGE</div>
    <svg class="promo-tails" viewBox="0 0 540 50">
      <polygon points="0,12 40,12 40,44 0,44 12,28" fill="#ffffff"/>
      <polygon points="540,6 500,6 500,38 540,38 528,22" fill="#ffffff"/>
    </svg>
    <div class="headline headline--promo">PROMO!</div>
    <div class="promo-rule"></div>

    <div class="food-photo" role="img" aria-label="Photo of a salad bowl, a double cheeseburger and a slice of carrot cake"></div>

    <section class="offer">
      <div class="gift-card">
        <div class="gift-card__band-v"></div>
        <div class="gift-card__band-h"></div>
        <div class="gift-card__label">GIFT CARD</div>
        <div class="gift-card__name">VERANDEL</div>
        <div class="gift-card__tag">HEALTHY KITCHEN | MEAL PREP</div>
      </div>
      <div class="offer__box">
        <p class="offer__lead">BUY OUR HOLIDAY<br>PACKAGE OF $500 &amp;</p>
        <p class="offer__reward">RECEIVE A $100<br>GIFT CARD!</p>
      </div>
    </section>

    <footer class="footer">
      <div class="brand">
        <div class="brand__row"><span class="brand__dot"></span><span class="brand__name">VERANDEL</span></div>
        <span class="brand__tag">HEALTHY KITCHEN | MEAL PREP</span>
      </div>
      <div class="footer__note">
        <p class="footer__claim">OUR BIGGEST PROMO TO DATE.</p>
        <p class="footer__date">Offer ends December 31st, 2022.</p>
      </div>
    </footer>
  </main>
</body>
</html>
```